Chart a Bright Path

We need a website designed for a life coaching company who specialises in one on one coaching, workshops and seminars where they teach participants in goal setting and how to achieve them for a better life.

Objectives

·         Easy to use

·         Clear & concise

·         Quality but not too flashy

·         Shows clearly what you do and how you interact with clients

·         No fuss, straight up

·         Gives those who hear your name or business name a place to go to obtain further information on what I am doing, why & how they can use my services.

·         A way for clients to contact you

·         Seminar & workshop bookings (not mandatory)

·         Most of the website to be static.

Number of Pages Required

1 page

Requirements
Must have
• Sitemap

• Home
• About Us
• One on One Coaching
• Workshops/Seminars
• How we Work?
• Pricing
• Testimonials
• Contact Us

• Design/Content Brief

• ü  The following elements are included in the design/content brief which this proposal is based on:

• o    Flash banner with some images rotating that reflect your business.

• o    Logo and phone number 0498 736 210 will be prominently displayed.

• o    Horizontal Navigation

• o    Contact Us icon on homepage

• o    Sign up for our newsletter on homepage

• o    Privacy Policy/Sitemap/Terms & Conditions in footer

• o    - larger rounded buttons

• o    - good size font

• o    - not having to scroll too far

• o    - soft feel, but not fluffy (images will enhance this)

• ü  Colours that could be used with logo

• o   What about this?  RGB 128,128,128

• o   What about this?  RGB 54, 95, 145

• o   What about this?  RGB 51, 204, 51

• o   Red – R255

• ü   http://www.velmorin.com/

• o    I like this website and its rounded buttons, large easy to see and use.

• o    Soft colours

• o    Changing pictures at the top of screen

```html
<!DOCTYPE html>
<html lang="en">
<head>
<meta charset="utf-8">
<title>Chart a Bright Path</title>
<link rel="stylesheet" href="https://fonts.googleapis.com/css2?family=Montserrat:wght@300;400;500;600&display=swap">
<style>
:root{
  --red:#e3000f;
  --red-dark:#c8101b;
  --red-light:#ff4a4f;
  --ink:#111111;
  --white:#ffffff;
  --bg-outer:#d9dadb;
  --bg-inner:#f6f6f6;
  --grey-box:#bdbec1;
  --footer:#000000;
}
*{margin:0;padding:0;box-sizing:border-box}
html,body{width:1200px;height:1091px;overflow:hidden}
body{
  background:radial-gradient(ellipse at 50% 50%,var(--bg-inner) 40%,var(--bg-outer) 100%);
  font-family:"Montserrat",Arial,sans-serif;
  color:var(--ink);
  position:relative;
}
.page{
  position:absolute;left:97px;top:0;width:1008px;height:1025px;
  background:var(--white);border-radius:0 0 12px 12px;
  box-shadow:0 0 18px rgba(0,0,0,.25);
}
.brand{position:absolute;left:30px;top:44px;display:flex;align-items:center;gap:14px}
.brand-dot{width:30px;height:30px;border-radius:50%;background:var(--red)}
.brand-name{font-size:31px;font-weight:600;color:var(--red);letter-spacing:.3px}
.callbox{
  position:absolute;left:759px;top:0;width:236px;height:74px;
  background:linear-gradient(#cfd0d2,var(--grey-box));
  border-radius:0 0 10px 10px;color:var(--white);text-align:center;
  padding-top:17px;line-height:23px;
}
.callbox .label{font-size:19px;font-weight:300}
.callbox .phone{font-size:19px;font-weight:500}
.banner{
  position:absolute;left:13px;top:122px;width:982px;height:188px;border-radius:12px;overflow:hidden;
  background:linear-gradient(180deg,#79bff0 0%,#a9d7f5 62%,#b8d99c 82%,#5b8a2c 100%);
}
.banner-tagline{position:absolute;left:335px;top:67px;font-size:30px;font-weight:400;color:var(--ink);letter-spacing:.6px}
.nav{position:absolute;left:13px;top:323px;display:grid;grid-template-columns:repeat(4,236px);column-gap:13px;row-gap:13px}
.nav-button{
  position:relative;height:87px;border-radius:10px;
  background:linear-gradient(var(--red) 0%,var(--red-dark) 100%);
  display:flex;align-items:center;justify-content:center;text-align:center;
  color:var(--white);font-size:26px;font-weight:300;line-height:26px;overflow:hidden;
  padding-top:4px;
}
.nav-button::before{
  content:"";position:absolute;left:6px;right:6px;top:6px;height:44px;
  border-radius:8px 8px 50% 50% / 8px 8px 22px 22px;
  background:linear-gradient(var(--red-light),#f23a40);opacity:.8;
}
.nav-button span{position:relative}
.intro{position:absolute;left:40px;top:554px;width:692px}
.intro-heading{font-size:39px;font-weight:300;color:var(--red);line-height:41px;margin-bottom:16px}
.intro-heading strong{font-weight:600}
.intro p{font-size:18.5px;line-height:26.2px;text-align:justify;margin-bottom:26px;font-weight:400}
.aside-link{position:absolute;width:200px;left:773px;text-align:center;font-size:18.5px;font-weight:500;line-height:20px}
.aside-contact{top:622px}
.aside-news{top:736px}
.aside-link svg{display:block;margin:0 auto 8px}
.footer{
  position:absolute;left:0;top:982px;width:1008px;height:43px;background:var(--footer);
  border-radius:0 0 12px 12px;color:var(--white);font-size:15px;font-weight:500;
  display:flex;align-items:center;justify-content:space-between;padding:0 18px 0 14px;
}
.footer-links span.sep{color:var(--red);margin:0 10px}
</style>
</head>
<body>
<div class="page">
  <div class="brand"><div class="brand-dot"></div><div class="brand-name">Chart a Bright Path</div></div>
  <div class="callbox"><div class="label">Call us anytime</div><div class="phone">0498 736 210</div></div>

  <div class="banner" role="img" aria-label="Photo of a woman relaxing on grass under a clear blue sky">
    <div class="banner-tagline">Achieve your goals for a better life</div>
  </div>

  <nav class="nav">
    <div class="nav-button"><span>Home</span></div>
    <div class="nav-button"><span>About Us</span></div>
    <div class="nav-button"><span>One on One<br>Coaching</span></div>
    <div class="nav-button"><span>Workshops &amp;<br>Seminars</span></div>
    <div class="nav-button"><span>How we work</span></div>
    <div class="nav-button"><span>Pricing</span></div>
    <div class="nav-button"><span>Testimonials</span></div>
    <div class="nav-button"><span>Contact Us</span></div>
  </nav>

  <section class="intro">
    <h1 class="intro-heading">We help you <strong>set positive goals</strong> to help better your life.</h1>
    <p>Lorem ipsum dolor sit amet, consectetur adipiscing elit. Fusce volutpat pulvinar enim. Praesent sit amet nisi metus. In hac habitasse platea dictumst. Ut sodales erat ac sem mattis vel mollis erat blandit. Donec convallis porttitor nunc, sed euismod nisl consequat non.</p>
    <p>Ut nec mauris ante. Suspendisse potenti. Class aptent taciti sociosqu ad litora torquent per conubia nostra, per inceptos himenaeos.</p>
    <p>Aliquam eu ipsum metus, a porta tellus. Duis tellus risus, dignissim et porttitor quis, pretium fermentum nisi. Aliquam erat volutpat. Quisque quam neque, dapibus in malesuada at, congue vitae ipsum.</p>
  </section>

  <div class="aside-link aside-contact">
    <svg width="78" height="44" viewBox="0 0 78 44"><rect x="1" y="1" width="76" height="42" rx="3" fill="#e3000f" stroke="#b0000a"/><path d="M3 3 L39 26 L75 3" fill="none" stroke="#fff" stroke-width="2.5"/><path d="M3 41 L28 20 M75 41 L50 20" stroke="#ff8a8e" stroke-width="1.5"/></svg>
    Contact Us
  </div>
  <div class="aside-link aside-news">
    <svg width="78" height="84" viewBox="0 0 78 84"><rect x="1" y="1" width="76" height="82" rx="4" fill="#e3000f" stroke="#b0000a"/><g stroke="#fff" stroke-width="2"><line x1="8" y1="12" x2="60" y2="12"/><line x1="8" y1="19" x2="68" y2="19"/><line x1="8" y1="26" x2="54" y2="26"/><line x1="8" y1="40" x2="70" y2="40"/><line x1="8" y1="47" x2="62" y2="47"/><line x1="8" y1="60" x2="70" y2="60"/><line x1="8" y1="67" x2="40" y2="67"/></g></svg>
    Sign up for<br>our newsletter
  </div>

  <footer class="footer">
    <div>©2009 Chart a Bright Path</div>
    <div class="footer-links">Privacy Policy<span class="sep">|</span>Sitemap<span class="sep">|</span>Terms &amp; Conditions</div>
  </footer>
</div>
</body>
</html>
```